Shine the Light - Brochure Design for Exquisite Lighting Range

I would love a brochure design that is
Cool
High End
Pushes Boundaries

The Product:
Beautifully crafted lighting range of pendants and chandeliers constructed from Black Walnut, American Ash, Mahogany.
Specifically designed for calming spaces using a rough luxe aesthetic.
Award winning design exhibited at Foire du Vitrail.
World class product range covering modern, traditional French and English Country style
Retails to resort contractors and retailers in Europe and Southeast Asia, among others
Selling limited quantity of stock

Target Market(s)

Interior Designers
Architects
Builders
Homewares Retailers
Home-owners

Industry/Entity Type

Interior Decoration

Font styles to use
Serif
Sans Serif

Colors

Designer to choose only greyscale colors for use in the design.

Requirements
Must have
• Visual impact telling the story of luxury
• All details supplied covering lighting dimensions and materials
• Brochure to be suitable for print media and digital format
• Clear layout
• Strong modern font
• Interesting/compelling to look at
• Subdued sophisticated colour palette
• Strong contrasts
Nice to have
• Some interesting graphics that I would never have thought of
• Layout that is super engaging
• Push the boundaries
Should not have
• Clutter
• Too much detail

```html
<!DOCTYPE html>
<html lang="en">
<head>
<meta charset="utf-8">
<title>Ondine — Lighting Collection Spread</title>
<link rel="stylesheet" href="https://fonts.googleapis.com/css2?family=Cinzel:wght@400&family=Open+Sans:ital,wght@0,400;1,400&display=swap">
<style>
  :root {
    --backdrop: #d9d9d9;
    --paper: #efefef;
    --band: #383636;
    --band-soft: #5a5858;
    --ink-light: #f2f2f2;
    --ink-muted: #bdbdbd;
    --studio-deep: #3e3e3e;
    --studio-dark: #555555;
    --studio-mid: #7d7d7d;
    --studio-light: #b4b4b4;
    --walnut: rgba(92, 58, 36, .55);
    --walnut-glow: rgba(214, 170, 120, .35);
    --iron: rgba(20, 20, 20, .35);
  }
  * { box-sizing: border-box; margin: 0; padding: 0; }
  html, body { width: 1200px; height: 880px; overflow: hidden; }
  body { background: var(--backdrop); position: relative; font-family: "Open Sans", sans-serif; }

  .spread {
    position: absolute; left: 60px; top: 140px;
    width: 1080px; height: 600px;
    display: flex;
    box-shadow: 0 10px 30px rgba(0,0,0,.18);
  }
  .page { position: relative; width: 540px; height: 600px; background: var(--paper); }
  .page--left::after, .page--right::after {
    content: ""; position: absolute; top: 0; bottom: 0; width: 22px; z-index: 2; pointer-events: none;
  }
  .page--left::after { right: 0; background: linear-gradient(to right, rgba(0,0,0,0), rgba(0,0,0,.16)); }
  .page--right::after { left: 0; background: linear-gradient(to left, rgba(0,0,0,0), rgba(0,0,0,.16)); }

  .band {
    position: absolute; top: 0; bottom: 0;
    width: 170px; background: var(--band);
    padding: 30px 20px;
  }
  .page--left .band { left: 36px; }
  .page--right .band { right: 36px; }

  .brand {
    display: flex; align-items: center; gap: 8px;
    color: var(--ink-light);
    font-size: 15px; letter-spacing: 2px;
  }
  .brand__mark { width: 12px; height: 12px; background: var(--band-soft); }

  .product { position: absolute; left: 20px; right: 14px; color: var(--ink-light); }
  .page--left .product { top: 300px; }
  .page--right .product { top: 370px; }
  .product__name {
    font-family: "Cinzel", serif; font-size: 15px; line-height: 1.25;
    letter-spacing: 1px; margin-bottom: 12px;
  }
  .product__specs { font-size: 8.5px; line-height: 1.45; }
  .product__specs dt { font-style: italic; color: var(--ink-muted); }
  .product__specs dd { color: var(--ink-light); }

  .photo { position: absolute; top: 150px; height: 290px; }
  .photo--calder {
    left: 290px; width: 250px;
    background:
      radial-gradient(ellipse 48% 26% at 55% 40%, var(--walnut-glow), rgba(0,0,0,0) 70%),
      radial-gradient(ellipse 60% 40% at 55% 42%, var(--walnut), rgba(0,0,0,0) 75%),
      radial-gradient(ellipse 80% 60% at 50% 100%, rgba(0,0,0,.25), rgba(0,0,0,0) 70%),
      radial-gradient(ellipse at 55% 35%, var(--studio-mid), var(--studio-dark) 60%, var(--studio-deep));
  }
  .photo--marlow {
    left: 0; width: 300px;
    background:
      radial-gradient(ellipse 55% 24% at 52% 46%, var(--iron), rgba(0,0,0,0) 72%),
      radial-gradient(ellipse 70% 55% at 50% 100%, rgba(0,0,0,.2), rgba(0,0,0,0) 70%),
      radial-gradient(ellipse at 40% 30%, var(--studio-light), var(--studio-mid) 55%, var(--studio-dark));
  }
</style>
</head>
<body>
  <main class="spread">
    <section class="page page--left">
      <aside class="band">
        <div class="brand"><span class="brand__mark"></span>ondine</div>
        <div class="product">
          <h2 class="product__name">Calder<br>Chandelier II</h2>
          <dl class="product__specs">
            <dt>Finish</dt>
            <dd>Light Oil Stain on Wood, Worn Black Iron on Metal (LOSF/WBI)</dd>
            <dt>Materials</dt>
            <dd>Gmelina Wood &amp; Metal, Black Cloth Shades, CE Electrical Fittings</dd>
            <dt>Dimensions</dt>
            <dd>976Ø x 993H mm</dd>
          </dl>
        </div>
      </aside>
      <div class="photo photo--calder" role="img" aria-label="Calder Chandelier II: walnut-stained wood and worn iron chandelier with dark cloth shades, lit on a grey studio backdrop"></div>
    </section>

    <section class="page page--right">
      <div class="photo photo--marlow" role="img" aria-label="Marlow Chandelier (L): two-tier worn black iron candle chandelier, lit on a pale grey studio backdrop"></div>
      <aside class="band">
        <div class="brand"><span class="brand__mark"></span>ondine</div>
        <div class="product">
          <h2 class="product__name">Marlow<br>Chandelier (L)</h2>
          <dl class="product__specs">
            <dt>Finish</dt>
            <dd>Worn Black Iron Finish (WBI)</dd>
            <dt>Materials</dt>
            <dd>Metal &amp; CE Electrical Fittings</dd>
            <dt>Dimensions</dt>
            <dd>1600 Ø x 1207H mm</dd>
          </dl>
        </div>
      </aside>
    </section>
  </main>
</body>
</html>
```